KB Rubbish Removal Business Card

Hey,
I need a double sided business card designed for a rubbish removal business based in Australia. Logo is already chosen, similar colours preferred for both sides of the business card.

Details to include:

Front:

KB Rubbish Removal
Darren Holloway
Managing Director
Mobile: 0471 902 146
Email: darren@kbrubbishremoval.com.au
Website: kbrubbishremoval.com.au

Rear:

How did we do?
kbrubbishremoval.com.au/review

```html
<!DOCTYPE html>
<html lang="en">
<head>
<meta charset="utf-8">
<title>KB Rubbish Removal – Business Card</title>
<link rel="stylesheet" href="https://fonts.googleapis.com/css2?family=Lato:wght@400;700;900&family=Raleway:wght@500;700&display=swap">
<style>
  :root {
    --green-brand: #1a7f3c;
    --green-mid: #27a844;
    --green-dark: #146b35;
    --lime: #b5d63f;
    --lime-soft: #5bbf4a;
    --text-grey: #505050;
    --name-grey: #4a4a4a;
    --page: #f2f2f2;
    --card: #ffffff;
  }
  * { box-sizing: border-box; margin: 0; padding: 0; }
  html, body { width: 820px; height: 1200px; overflow: hidden; }
  body {
    background: var(--page);
    font-family: "Lato", sans-serif;
    position: relative;
  }
  .card {
    position: absolute;
    left: 50px;
    width: 720px;
    height: 411px;
    background: var(--card);
    box-shadow: 0 2px 10px rgba(0,0,0,0.18);
    overflow: hidden;
  }
  .card--front { top: 150px; }
  .card--rear { top: 630px; }

  .brand { position: absolute; display: flex; align-items: center; }
  .brand__dot { border-radius: 50%; background: var(--green-mid); flex: none; }
  .brand__name { font-weight: 700; color: var(--green-brand); white-space: nowrap; }

  .card--front .brand { left: 42px; top: 36px; height: 112px; }
  .card--front .brand__dot { width: 96px; height: 96px; margin-right: 44px; }
  .card--front .brand__name { font-size: 36px; }

  .card--rear .brand { left: 58px; top: 112px; height: 146px; }
  .card--rear .brand__dot { width: 138px; height: 138px; margin-right: 44px; }
  .card--rear .brand__name { font-size: 46px; }

  .review { position: absolute; left: 240px; top: 262px; font-family: "Raleway", sans-serif; }
  .review__prompt { font-weight: 700; font-size: 22px; color: var(--name-grey); line-height: 1.2; }
  .review__link { font-family: "Lato", sans-serif; font-weight: 400; font-size: 19px; color: var(--text-grey); margin-top: 4px; }

  .person { position: absolute; right: 41px; top: 170px; text-align: right; font-family: "Raleway", sans-serif; }
  .person__name { font-weight: 700; font-size: 28px; color: var(--name-grey); line-height: 1.05; }
  .person__role { font-weight: 500; font-size: 19px; color: var(--text-grey); margin-top: 2px; }

  .rule {
    position: absolute; left: 0; top: 214px; width: 502px; height: 2px;
    background: linear-gradient(90deg, var(--green-mid), var(--lime) 55%, var(--green-mid));
  }

  .contacts { position: absolute; left: 40px; top: 250px; list-style: none; }
  .contacts li { display: flex; align-items: center; height: 37.5px; font-size: 21px; color: var(--text-grey); }
  .contacts svg { width: 24px; height: 24px; margin-right: 9px; flex: none; }

  .band { position: absolute; left: 0; bottom: 0; width: 100%; height: 25px; display: flex; }
  .band span { flex: 1; }
  .band__dark { background: linear-gradient(90deg, var(--green-mid), var(--green-dark)); }
  .band__light { background: linear-gradient(90deg, var(--lime), var(--lime-soft)); }
  .band--rear .band__dark { background: linear-gradient(90deg, var(--green-dark), var(--green-mid)); }
  .band--rear .band__light { background: linear-gradient(90deg, var(--lime-soft), var(--lime)); }
</style>
</head>
<body>

<section class="card card--front" aria-label="Business card front">
  <div class="brand">
    <span class="brand__dot"></span>
    <span class="brand__name">KB Rubbish Removal</span>
  </div>

  <div class="person">
    <p class="person__name">Darren Holloway</p>
    <p class="person__role">Managing Director</p>
  </div>
  <div class="rule"></div>

  <ul class="contacts">
    <li>
      <svg viewBox="0 0 24 24" aria-hidden="true"><rect width="24" height="24" fill="#1a7f3c"/><rect x="8" y="5" width="8" height="14" rx="1.5" fill="none" stroke="#fff" stroke-width="2"/><rect x="10.5" y="15.5" width="3" height="1.5" fill="#fff"/></svg>
      0471 902 146
    </li>
    <li>
      <svg viewBox="0 0 24 24" aria-hidden="true"><rect width="24" height="24" fill="#1a7f3c"/><rect x="4.5" y="7" width="15" height="10" fill="none" stroke="#fff" stroke-width="1.6"/><path d="M4.5 7l7.5 6 7.5-6M4.5 17l5.5-5M19.5 17l-5.5-5" fill="none" stroke="#fff" stroke-width="1.4"/></svg>
      darren@kbrubbishremoval.com.au
    </li>
    <li>
      <svg viewBox="0 0 24 24" aria-hidden="true"><rect width="24" height="24" fill="#1a7f3c"/><circle cx="12" cy="12" r="7" fill="none" stroke="#fff" stroke-width="1.5"/><ellipse cx="12" cy="12" rx="3" ry="7" fill="none" stroke="#fff" stroke-width="1.3"/><path d="M5 12h14M6 8.5h12M6 15.5h12" stroke="#fff" stroke-width="1.2"/></svg>
      kbrubbishremoval.com.au
    </li>
  </ul>

  <div class="band"><span class="band__dark"></span><span class="band__light"></span></div>
</section>

<section class="card card--rear" aria-label="Business card rear">
  <div class="brand">
    <span class="brand__dot"></span>
    <span class="brand__name">KB Rubbish Removal</span>
  </div>
  <div class="review">
    <p class="review__prompt">How did we do?</p>
    <p class="review__link">kbrubbishremoval.com.au/review</p>
  </div>
  <div class="band band--rear"><span class="band__light"></span><span class="band__dark"></span></div>
</section>

</body>
</html>
```